Business Card: RW Office Partners - Your tidy answer finder

Business Name: RW Office Partners
Website: www.rwofficepartners.com.au
Email: marisol@rwofficepartners.com.au
Mobile: 61 487 902 346
Facebook: @rwofficepartners
Instrgram: @rwofficepartners

Brading Colours:
HEX
#986474
#ddccd3
#7a8498
#c9d8e4
#000000
#ffffff

Tag Line: Your organised problem solver

Link to DRAFT website:
https://helpdeskhub.sitebuilderx.com/rw-office-partners

About Page from the website:
My name is Marisol Bramwell, and I would love to assist you to become more productive in your day to day and achieve your business and personal goals.
My mission is to give you time, time to work on the important tasks of your business or to be able to spend more time with your family. I will take on the tasks you don’t have time for, don’t know well or simply don’t like to do.
I have an extensive background in Administration, Tender Coordination, Document Control, WHS and Quality Management working primarily in the Construction, Mining and Corporate World.
I am passionate about being organised, having order and making things in your life (and mine) easier! I love to watch something unfold and grow into something amazing! I am known for being the go-to problem solver, the organiser of all things, producing high standards of work even under pressure. I’m also a confident communicator, and I understand that you’re busy running your business.

Target Market(s)

Small to Medium Business who require assistance in their business by a virtual assistant.

Industry/Entity Type

Virtual Assistant

Contact Information for Business Card

Mobile: 61 487 902 346

Font styles to use
Sans Serif

Colors
ffffff

Requirements
Must have
• Branding Colours as outlined.
Contact Details as outlined.
Logo as provided.
Proper contact details - mobile, facebook, instragm, website.
Simple, Elegant, very clean looking.
Should not have
• Note cute with pictures.
Not too girly as still want to market to construction companies.

```html
<!DOCTYPE html>
<html lang="en">
<head>
<meta charset="utf-8">
<title>RW Office Partners – Business Card</title>
<link rel="stylesheet" href="https://fonts.googleapis.com/css2?family=Montserrat:wght@400;500;600&display=swap">
<style>
  :root {
    --slate: #7a8498;
    --mauve: #986474;
    --white: #ffffff;
    --ink: #2c2c30;
    --backdrop: #e4e4e4;
    --rule-light: #ffffff;
  }
  * { margin: 0; padding: 0; box-sizing: border-box; }
  html, body {
    width: 1200px;
    height: 1200px;
    overflow: hidden;
    background: var(--backdrop);
    font-family: "Montserrat", sans-serif;
  }
  .canvas { position: relative; width: 1200px; height: 1200px; }

  .card {
    position: absolute;
    left: 178px;
    width: 840px;
    height: 479px;
    overflow: hidden;
  }
  .card--front { top: 85px; background: var(--slate); }
  .card--back  { top: 595px; background: var(--white); }

  .wordmark {
    position: absolute;
    font-weight: 600;
    font-size: 46px;
    letter-spacing: 0.5px;
    line-height: 1;
    white-space: nowrap;
  }
  .card--front .wordmark { left: 281px; top: 235px; color: var(--white); }
  .card--back .wordmark  { left: 103px; top: 104px; color: var(--slate); }

  .front-rule {
    position: absolute;
    left: 281px;
    right: 0;
    top: 362px;
    height: 2px;
    background: var(--rule-light);
  }
  .tagline {
    position: absolute;
    left: 281px;
    top: 383px;
    color: var(--white);
    font-size: 27px;
    font-weight: 400;
  }

  .back-spine {
    position: absolute;
    left: 291px;
    top: 186px;
    bottom: 0;
    width: 2px;
    background: var(--mauve);
  }
  .contact-list {
    position: absolute;
    left: 280px;
    top: 265px;
    list-style: none;
  }
  .contact-item {
    display: flex;
    align-items: center;
    height: 35px;
    color: var(--ink);
    font-size: 20px;
    font-weight: 400;
  }
  .contact-icon {
    width: 24px;
    height: 24px;
    margin-right: 18px;
    flex: none;
  }
</style>
</head>
<body>
<main class="canvas">

  <section class="card card--front" aria-label="Card front">
    <div class="wordmark">RW Office Partners</div>
    <div class="front-rule"></div>
    <p class="tagline">Your tidy answer finder</p>
  </section>

  <section class="card card--back" aria-label="Card back">
    <div class="wordmark">RW Office Partners</div>
    <div class="back-spine"></div>
    <ul class="contact-list">
      <li class="contact-item">
        <svg class="contact-icon" viewBox="0 0 24 24" aria-hidden="true">
          <circle cx="12" cy="12" r="12" fill="#7a8498"/>
          <rect x="9" y="5.5" width="6" height="13" rx="1" fill="none" stroke="#fff" stroke-width="1.4"/>
          <circle cx="12" cy="16.2" r="0.8" fill="#fff"/>
        </svg>
        <span>61 487 902 346</span>
      </li>
      <li class="contact-item">
        <svg class="contact-icon" viewBox="0 0 24 24" aria-hidden="true">
          <circle cx="12" cy="12" r="12" fill="#7a8498"/>
          <rect x="6" y="8" width="12" height="8.5" fill="none" stroke="#fff" stroke-width="1.4"/>
          <path d="M6 8 L12 13 L18 8" fill="none" stroke="#fff" stroke-width="1.4"/>
        </svg>
        <span>marisol@rwofficepartners.com.au</span>
      </li>
      <li class="contact-item">
        <svg class="contact-icon" viewBox="0 0 24 24" aria-hidden="true">
          <circle cx="12" cy="12" r="12" fill="#7a8498"/>
          <circle cx="12" cy="12" r="6" fill="none" stroke="#fff" stroke-width="1.4"/>
          <ellipse cx="12" cy="12" rx="2.6" ry="6" fill="none" stroke="#fff" stroke-width="1.2"/>
          <path d="M6 12 H18" stroke="#fff" stroke-width="1.2"/>
        </svg>
        <span>www.rwofficepartners.com.au</span>
      </li>
      <li class="contact-item">
        <svg class="contact-icon" viewBox="0 0 24 24" aria-hidden="true">
          <circle cx="12" cy="12" r="12" fill="#7a8498"/>
        </svg>
        <span>@rwofficepartners</span>
      </li>
      <li class="contact-item">
        <svg class="contact-icon" viewBox="0 0 24 24" aria-hidden="true">
          <circle cx="12" cy="12" r="12" fill="#7a8498"/>
        </svg>
        <span>@rwofficepartners</span>
      </li>
    </ul>
  </section>

</main>
</body>
</html>
```